Business Card & Stationary
For Event Planning Website
I need single sided standard sized Business Card [3.5" x 2"]
Same as logo or similar
Professional
First Name Last Name
Founder & Chief Executive Officer
Address 1
Address 2
New York, NY 10016
xyz@juniperhours.com
www.juniperhours.com
Feel free to be creative - the site is for party planning (weddings, bar-mitzvahs, etc.) so it should be modern & professional, with a fun factor.
I used test data to protect personal data but I can supply you with all of the information you need later.
I'm not sure which eps file corresponds to the jpg.
This is the hamsa (hand) which is part of the logo
The hand - ai file
Webpage Background Pattern

```html
<!DOCTYPE html>
<html lang="en">
<head>
<meta charset="utf-8">
<title>JuniperHours Business Card</title>
<link href="https://fonts.googleapis.com/css2?family=Quicksand:wght@500;700&family=Open+Sans:wght@400;700&display=swap" rel="stylesheet">
<style>
  :root {
    --brand-blue: #1f86d3;
    --card-back: #2b8ad4;
    --card-front: #ffffff;
    --text-grey: #6b6f74;
    --stage: #e6e7e9;
  }
  html, body {
    margin: 0;
    padding: 0;
    width: 1200px;
    height: 926px;
    overflow: hidden;
    background: var(--stage);
  }
  .canvas {
    position: relative;
    width: 1200px;
    height: 926px;
  }
  .card {
    position: absolute;
    top: 320px;
    width: 500px;
    height: 286px;
    border-radius: 24px;
    box-shadow: 0 6px 18px rgba(0,0,0,0.18);
    box-sizing: border-box;
  }
  .card-front {
    left: 80px;
    background: var(--card-front);
    padding: 34px 36px;
  }
  .card-back {
    left: 620px;
    background: var(--card-back);
  }
  .brand {
    position: absolute;
    top: 42px;
    right: 36px;
    display: flex;
    align-items: center;
    gap: 10px;
  }
  .brand-name {
    font-family: "Quicksand", sans-serif;
    font-weight: 500;
    font-size: 38px;
    letter-spacing: -0.5px;
    color: var(--brand-blue);
    line-height: 1;
  }
  .brand-dot {
    width: 22px;
    height: 22px;
    border-radius: 50%;
    background: var(--brand-blue);
  }
  .person {
    position: absolute;
    left: 36px;
    top: 150px;
  }
  .person-name {
    font-family: "Open Sans", sans-serif;
    font-weight: 700;
    font-size: 19px;
    color: var(--brand-blue);
    margin: 0;
  }
  .person-title {
    font-family: "Open Sans", sans-serif;
    font-size: 11px;
    color: var(--text-grey);
    margin: 2px 0 0;
  }
  .contact {
    position: absolute;
    left: 36px;
    top: 206px;
    display: flex;
    gap: 28px;
    font-family: "Open Sans", sans-serif;
    font-size: 8.5px;
    line-height: 1.45;
    color: var(--text-grey);
  }
  .contact p { margin: 0; }
  .contact .label { color: var(--brand-blue); font-weight: 700; }
</style>
</head>
<body>
<main class="canvas">
  <section class="card card-front" aria-label="Business card front">
    <div class="brand">
      <span class="brand-name">juniperhours</span>
      <span class="brand-dot"></span>
    </div>
    <div class="person">
      <p class="person-name">Dara Felton</p>
      <p class="person-title">Founder &amp; Chief Executive Officer</p>
    </div>
    <div class="contact">
      <div class="contact-address">
        <p>Address 1</p>
        <p>Address 2</p>
        <p>New York, NY 10016</p>
        <p><span class="label">E</span> xyz@juniperhours.com</p>
        <p><span class="label">W</span> www.juniperhours.com</p>
      </div>
      <div class="contact-phone">
        <p><span class="label">T</span> 555 010 2040</p>
        <p><span class="label">F</span> 555 010 2041</p>
      </div>
    </div>
  </section>
  <section class="card card-back" aria-label="Business card back"></section>
</main>
</body>
</html>
```